Pamphlet for IT Services Company (MSP Provider or Managed Services Provider)

We need a pamphlet designed for our Managed Services Company. We are an established company of 17 years that has never advertised. We'd like a pamphlet that we can drop off at potential client sites that describes our services. I like clean and prefer Orange as an accent color. We'd like to touch on the fact that we cater to our clients needs and go above and beyond what the other providers do.

Target Market(s)

Small and Medium Sized Businesses

Industry/Entity Type

It Service

Font styles to use
Other font styles liked:
• Try to match font on logo or website

Requirements
Must have
• Must highlight with the following Services and descriptions with Logo
Managed IT Services
IT Support
VOIP Solutions
WiFI Solutions
Contact information with phone number and website address.
Please view website korvanetpro.com
try to match fons on website above.
Nice to have
• Customer Testimonials. May a couple one line testimonials. Not real sure because this is the first time we've ever designed a brochure.
Should not have
• Not Sure

```html
<!DOCTYPE html>
<html lang="en">
<head>
<meta charset="utf-8">
<title>Korvanet Pro – Managed IT Services</title>
<link rel="stylesheet" href="https://fonts.googleapis.com/css2?family=Oswald:wght@500;600;700&family=Montserrat:wght@500;600;700;800&family=Dosis:wght@400;500&family=Nunito+Sans:wght@400&family=Quicksand:wght@500&display=swap">
<style>
  :root {
    --orange: #f28a1e;
    --orange-soft: #f3964a;
    --orange-deep: #e97c23;
    --navy: #1b2435;
    --slate: #4d5b6d;
    --slate-icon: #5e6d80;
    --ink: #1a1a1a;
    --body: #3a3a3a;
    --rule: #f6c79a;
    --strip: #f2f2f2;
    --page: #d9d9d9;
    --white: #ffffff;
  }
  * { box-sizing: border-box; margin: 0; padding: 0; }
  html, body { width: 984px; height: 1200px; overflow: hidden; background: var(--page); }
  .flyer {
    position: absolute; left: 67px; top: 0; width: 849px; height: 1200px;
    background: var(--white); overflow: hidden;
    font-family: "Nunito Sans", sans-serif;
  }
  .hero-art { position: absolute; left: 0; top: 0; }
  .brand {
    position: absolute; left: 54px; top: 44px;
    display: flex; align-items: center; gap: 12px;
    font-family: "Quicksand", sans-serif; font-weight: 500;
    font-size: 38px; color: var(--orange); letter-spacing: 0.5px;
  }
  .brand-dot { width: 26px; height: 26px; border-radius: 50%; border: 3px solid var(--orange); }
  .headline {
    position: absolute; left: 46px; top: 130px;
    font-family: "Oswald", sans-serif; font-weight: 700; line-height: 0.98;
  }
  .headline .line-accent { display: block; font-size: 56px; color: var(--orange); letter-spacing: 1px; }
  .headline .line-main { display: block; font-size: 66px; color: var(--white); letter-spacing: 0.5px; }
  .tagline {
    position: absolute; left: 38px; top: 300px; width: 310px;
    font-family: "Montserrat", sans-serif; font-weight: 700;
    font-size: 22px; line-height: 32px; color: var(--ink);
  }
  .section-tab {
    position: absolute; left: 37px; top: 487px; width: 234px; height: 54px;
    background: var(--orange); color: var(--white);
    font-family: "Oswald", sans-serif; font-weight: 600; font-size: 33px;
    display: flex; align-items: center; justify-content: center; letter-spacing: 0.5px;
  }
  .rule-h { position: absolute; height: 2px; background: var(--rule); }
  .rule-v { position: absolute; width: 2px; background: var(--rule); left: 432px; top: 521px; height: 492px; }
  .service { position: absolute; left: 0; width: 430px; }
  .service-icon {
    position: absolute; left: 36px; width: 77px; height: 77px; border-radius: 50%;
    display: flex; align-items: center; justify-content: center;
  }
  .service-icon.is-slate { background: var(--slate-icon); }
  .service-icon.is-orange { background: var(--orange-deep); }
  .service-text { position: absolute; left: 136px; width: 270px; }
  .service-title { font-family: "Dosis", sans-serif; font-weight: 500; font-size: 23px; color: var(--ink); line-height: 1.1; }
  .service-title.is-accent { color: var(--orange-deep); }
  .service-kicker { font-size: 6.5px; color: var(--body); margin-top: 3px; }
  .service-body { font-size: 9.8px; line-height: 13.8px; color: var(--body); margin-top: 6px; }
  .testimonial-title {
    position: absolute; left: 432px; width: 417px; top: 532px; text-align: center;
    font-family: "Montserrat", sans-serif; font-weight: 800; font-size: 35px; color: var(--ink);
  }
  .testimonial-frames { position: absolute; left: 0; top: 0; }
  .quote {
    position: absolute; border-radius: 14px; display: flex; align-items: center;
    padding: 0 14px; gap: 18px;
  }
  .quote.is-orange { background: var(--orange-soft); }
  .quote.is-orange.deep { background: var(--orange-deep); }
  .quote.is-slate { background: var(--slate); }
  .quote p {
    font-family: "Montserrat", sans-serif; font-weight: 500; font-size: 12.2px;
    line-height: 15.7px; color: var(--white); text-align: justify; width: 225px;
  }
  .avatar { width: 61px; height: 61px; border-radius: 50%; background: var(--white); display: flex; align-items: center; justify-content: center; flex: none; }
  .partners {
    position: absolute; left: 0; top: 1013px; width: 849px; height: 93px; background: var(--strip);
    display: flex; align-items: center; justify-content: space-around; padding: 0 30px;
  }
  .partner-badge { height: 30px; border-radius: 4px; background: #c9c9c9; }
  .partner-badge.dark { background: #4a4a4a; }
  .partner-badge.round { width: 34px; height: 34px; border-radius: 50%; background: #6a4c93; }
  .partner-badge.outline { width: 48px; height: 48px; background: transparent; border: 1px solid #bbb; }
  .footer-art { position: absolute; left: 0; top: 1106px; }
  .call { position: absolute; left: 27px; top: 1118px; display: flex; align-items: center; gap: 14px; }
  .call-label {
    position: absolute; left: 115px; top: 1118px; width: 170px; text-align: center;
    font-family: "Montserrat", sans-serif; font-weight: 700; font-size: 18px; color: var(--white);
  }
  .call-number {
    position: absolute; left: 88px; top: 1138px;
    font-family: "Oswald", sans-serif; font-weight: 600; font-size: 42px; color: var(--white); letter-spacing: 0.5px;
  }
  .contact { position: absolute; left: 462px; font-family: "Montserrat", sans-serif; font-weight: 700; font-size: 15.5px; color: var(--white); display: flex; align-items: center; gap: 10px; }
  .follow { position: absolute; left: 734px; top: 1125px; font-family: "Montserrat", sans-serif; font-weight: 700; font-size: 11px; color: var(--white); }
  .follow-icons { display: flex; gap: 12px; margin-top: 8px; margin-left: 4px; }
  .follow-icons span { width: 15px; height: 15px; border-radius: 50%; background: var(--orange); display: block; }
</style>
</head>
<body>
<div class="flyer">

  <svg class="hero-art" width="849" height="520" viewBox="0 0 849 520">
    <defs>
      <linearGradient id="heroPhoto" x1="0" y1="0" x2="1" y2="1">
        <stop offset="0" stop-color="#6b5446"/>
        <stop offset="0.45" stop-color="#9aa3a8"/>
        <stop offset="1" stop-color="#2d3136"/>
      </linearGradient>
    </defs>
    <rect x="0" y="0" width="849" height="274" fill="var(--navy)"/>
    <path d="M849 0 L849 100 C800 95 760 100 740 105 L849 0 Z" fill="var(--navy)"/>
    <path role="img" aria-label="Photo of an open laptop showing an analytics dashboard on a desk"
          d="M478 284 C412 298 372 350 372 405 C372 462 420 493 486 493 L849 493 L849 14 C742 14 662 72 632 168 L560 172 C520 205 505 262 478 284 Z"
          fill="url(#heroPhoto)"/>
    <path d="M484 282 C404 297 362 350 362 406 C362 468 420 503 492 503 L849 503" fill="none" stroke="var(--orange)" stroke-width="9"/>
    <path d="M849 6 C736 6 654 64 624 166" fill="none" stroke="var(--orange)" stroke-width="9"/>
  </svg>

  <div class="brand"><span class="brand-dot"></span>korvanet pro</div>

  <h1 class="headline">
    <span class="line-accent">MANAGED IT</span>
    <span class="line-main">SERVICES</span>
  </h1>

  <p class="tagline">A Simple, Cost Effective Plan for your ITInfrastructure. Wouldn't it be nice if your stuff just worked?</p>

  <div class="rule-h" style="left:0; top:521px; width:849px;"></div>
  <div class="section-tab">OUR SERVICES</div>
  <div class="rule-v"></div>

  <!-- Services -->
  <div class="service" style="top:560px;">
    <div class="service-icon is-slate" style="top:0;">
      <svg width="40" height="44" viewBox="0 0 40 44"><path d="M20 3 L36 9 V22 C36 32 28 39 20 41 C12 39 4 32 4 22 V9 Z" fill="none" stroke="#fff" stroke-width="4"/><path d="M20 9 L30 13 V22 C30 29 25 33 20 35 Z" fill="#fff"/></svg>
    </div>
    <div class="service-text" style="top:16px;">
      <div class="service-title">Managed IT</div>
      <div class="service-kicker">Let us take care of your ITLet us take care of your</div>
      <div class="service-body">Our MSP is a Flat Rate service that includes Onsite &amp; Remote Support, Endpoint Protection, Web Filtering, EncryptedOnline Backup &amp; Patch Management</div>
    </div>
  </div>
  <div class="rule-h" style="left:0; top:660px; width:432px;"></div>

  <div class="service" style="top:670px;">
    <div class="service-icon is-orange" style="top:0;">
      <svg width="40" height="40" viewBox="0 0 40 40"><path d="M9 20 C9 12 14 7 20 7 C26 7 31 12 31 20" fill="none" stroke="#fff" stroke-width="3"/><rect x="6" y="18" width="6" height="10" rx="2" fill="#fff"/><rect x="28" y="18" width="6" height="10" rx="2" fill="#fff"/><path d="M8 38 C8 31 13 28 20 28 C27 28 32 31 32 38 Z" fill="#fff"/></svg>
    </div>
    <div class="service-text" style="top:3px;">
      <div class="service-title is-accent">IT Support Services</div>
      <div class="service-body">We have a passion for what we do and it shows! Korvanet provides fast, reliable, expert solutions from experi-enced staff. You will never feel like just another client to us because our customers are family!</div>
    </div>
  </div>
  <div class="rule-h" style="left:0; top:765px; width:432px;"></div>

  <div class="service" style="top:773px;">
    <div class="service-icon is-orange" style="top:0;">
      <svg width="44" height="44" viewBox="0 0 44 44"><circle cx="22" cy="22" r="18" fill="#fff"/><path d="M15 13 L19 13 L20 18 L17.5 19.5 C19 23 21 25 24.5 26.5 L26 24 L31 25 L31 29 C31 30 30 31 29 31 C20 30 14 24 13 15 C13 14 14 13 15 13 Z" fill="var(--orange-deep)"/><path d="M25 14 A6 6 0 0 1 30 19 M25 10 A10 10 0 0 1 34 19" fill="none" stroke="var(--orange-deep)" stroke-width="2"/></svg>
    </div>
    <div class="service-text" style="top:10px;">
      <div class="service-title">VOIP Solutions</div>
      <div class="service-body">Phones are more than just an attachment to a desk. Allow us to help you maximize communication with your team and customers by using the latest technol-ogy that will likely save you money as well. Korvanet Pro partners with Calderline to provide phone hardware, systems, and phone service</div>
    </div>
  </div>
  <div class="rule-h" style="left:0; top:901px; width:432px;"></div>

  <div class="service" style="top:908px;">
    <div class="service-icon is-slate" style="top:0;">
      <svg width="46" height="40" viewBox="0 0 46 40"><path d="M4 14 A27 27 0 0 1 42 14" fill="none" stroke="#fff" stroke-width="4.5" stroke-linecap="round"/><path d="M11 21 A17 17 0 0 1 35 21" fill="none" stroke="#fff" stroke-width="4.5" stroke-linecap="round"/><path d="M17 28 A8 8 0 0 1 29 28" fill="none" stroke="#fff" stroke-width="4.5" stroke-linecap="round"/><circle cx="23" cy="35" r="3.5" fill="#fff"/></svg>
    </div>
    <div class="service-text" style="top:3px;">
      <div class="service-title is-accent">WiFi Solutions</div>
      <div class="service-body">WiFi is everywhere! (At least it should be.) Korvanet can extend your WiFi to cover your whole campus</div>
    </div>
  </div>

  <!-- Testimonials -->
  <h2 class="testimonial-title">TESTIMONIAL</h2>

  <svg class="testimonial-frames" width="849" height="1013" viewBox="0 0 849 1013">
    <path d="M773 608 H470 C456 608 448 616 448 630 V708 C448 722 456 733 470 733 H808 C822 733 830 742 830 756 V836 C830 850 822 857 808 857 H475 C461 857 453 865 453 879 V964 C453 978 461 987 475 987 H773" fill="none" stroke="var(--orange)" stroke-width="2"/>
    <circle cx="773" cy="608" r="7" fill="var(--orange-deep)"/>
    <circle cx="773" cy="987" r="7" fill="var(--orange-deep)"/>
  </svg>

  <div class="quote is-orange" style="left:462px; top:619px; width:345px; height:105px; padding-left:17px;">
    <p>Lorem Ipsum is simply dummy text of the printing and typesetting industry. Lorem Ipsum has been the industry's standard dummy text ever since the 1500s,</p>
    <div class="avatar"><svg width="32" height="34" viewBox="0 0 32 34"><circle cx="16" cy="10" r="8" fill="var(--orange-soft)"/><path d="M2 34 C2 24 8 20 16 20 C24 20 30 24 30 34 Z" fill="var(--orange-soft)"/></svg></div>
  </div>

  <div class="quote is-slate" style="left:451px; top:743px; width:346px; height:104px;">
    <div class="avatar"><svg width="32" height="34" viewBox="0 0 32 34"><circle cx="16" cy="10" r="8" fill="var(--slate)"/><path d="M2 34 C2 24 8 20 16 20 C24 20 30 24 30 34 Z" fill="var(--slate)"/></svg></div>
    <p style="margin-left:18px;">Lorem Ipsum is simply dummy text of the printing and typesetting industry. Lorem Ipsum has been the industry's standard dummy text ever since the 1500s,</p>
  </div>

  <div class="quote is-orange deep" style="left:458px; top:871px; width:346px; height:104px; padding-left:20px;">
    <p>Lorem Ipsum is simply dummy text of the printing and typesetting industry. Lorem Ipsum has been the industry's standard dummy text ever since the 1500s,</p>
    <div class="avatar"><svg width="32" height="34" viewBox="0 0 32 34"><circle cx="16" cy="10" r="8" fill="var(--orange-deep)"/><path d="M2 34 C2 24 8 20 16 20 C24 20 30 24 30 34 Z" fill="var(--orange-deep)"/></svg></div>
  </div>

  <!-- Partner badges -->
  <div class="partners" aria-label="Partner badges">
    <div class="partner-badge" style="width:146px; height:28px;"></div>
    <div class="partner-badge dark" style="width:112px; height:34px;"></div>
    <div class="partner-badge round"></div>
    <div class="partner-badge" style="width:106px; height:30px;"></div>
    <div class="partner-badge" style="width:82px; height:14px;"></div>
    <div class="partner-badge outline"></div>
  </div>

  <!-- Footer -->
  <svg class="footer-art" width="849" height="94" viewBox="0 0 849 94">
    <rect x="0" y="0" width="849" height="94" fill="var(--navy)"/>
    <polygon points="0,0 462,0 398,94 0,94" fill="var(--orange-deep)"/>
  </svg>

  <div class="call">
    <svg width="52" height="56" viewBox="0 0 52 56"><rect x="2" y="2" width="26" height="52" rx="4" fill="none" stroke="#fff" stroke-width="2.5"/><line x1="11" y1="8" x2="19" y2="8" stroke="#fff" stroke-width="2"/><circle cx="15" cy="47" r="2.5" fill="#fff"/><path d="M35 20 Q39 28 35 36 M41 16 Q47 28 41 40" fill="none" stroke="#fff" stroke-width="2.5"/></svg>
  </div>
  <div class="call-label">CALL US NOW</div>
  <div class="call-number">+1 (555) 014-2290</div>

  <div class="contact" style="top:1129px;">
    <svg width="18" height="18" viewBox="0 0 18 18"><circle cx="9" cy="9" r="7.5" fill="none" stroke="var(--orange)" stroke-width="1.5"/><ellipse cx="9" cy="9" rx="3.5" ry="7.5" fill="none" stroke="var(--orange)" stroke-width="1.5"/><line x1="1.5" y1="9" x2="16.5" y2="9" stroke="var(--orange)" stroke-width="1.5"/></svg>
    www.korvanetpro.com
  </div>
  <div class="contact" style="top:1160px;">
    <svg width="18" height="14" viewBox="0 0 18 14"><rect x="1" y="1" width="16" height="12" fill="none" stroke="var(--orange)" stroke-width="1.5"/><path d="M1 1 L9 8 L17 1" fill="none" stroke="var(--orange)" stroke-width="1.5"/></svg>
    info@korvanetpro.com
  </div>

  <div class="follow">Follow Us On
    <div class="follow-icons"><span></span><span></span><span></span></div>
  </div>

</div>
</body>
</html>
```